Create Label for Jojoba Oil and Argan Oil

We already have a logo design and we tried editing a label for pure Jojoba and Argan oils. We would like to have someone do two designs for our label.

We want people to distinguish between the two bottles of Argan and Jojoba but they must be on the same theme.

Also, we would like to have an elegant feel to the label.

Logo Design is attached in the files and some pictures of the bottles. The current labels are just their because we tried coming up with our own labels. You have freedom to change the look.

Target Market(s)

adult women and men

Industry/Entity Type

Cosmetic

Requirements
Must have
• The container uses Frosted glass as shown in pictures attached.
• Please do not change the shape of the Logo; although you have freedom to change the color.
• Designs must contain the following:
• For our Jojoba Oil:
• -- 100% Pure Jojoba Oil
• -- Face, Body & Hair
• -- 118 mL
• -- www.vorisalu.com
• -- Ingredient: Simmondsia Chinensis (Jojoba) Seed Oil
• -- For external use only
• -- must fit within 3" X 2.5" HIGH-GLOSS PAPER
• For our Argan Oil:
• -- 100% Pure Moroccan Argan Oil
• -- Face, Body & Hair
• -- 50 mL
• -- www.vorisalu.com
• -- Ingredient: Argania Spinosa (Argan) Kernel Oil
• -- must fit within 3.25" X 1.75" HIGH-GLOSS PAPER
Nice to have
• Must be good printed on High Gloss Paper and seen on a Website.

```html
<!DOCTYPE html>
<html lang="en">
<head>
<meta charset="utf-8">
<title>Vorisalu Oil Labels</title>
<link href="https://fonts.googleapis.com/css2?family=Mulish:wght@300;400;600;700&family=Great+Vibes&display=swap" rel="stylesheet">
<style>
  :root {
    --backdrop: #e6e7e8;
    --paper: #ffffff;
    --ink: #1a1a1a;
    --argan: #f7941d;
    --jojoba: #3db54a;
    --argan-art: linear-gradient(135deg, #f3f3f1 0%, #cfe8c6 55%, #6fbf5a 100%);
    --jojoba-art: linear-gradient(135deg, #f3f3f1 0%, #d6ecd0 50%, #5cb84a 100%);
  }
  * { box-sizing: border-box; margin: 0; padding: 0; }
  html, body { width: 1200px; height: 1200px; overflow: hidden; }
  body { background: var(--backdrop); position: relative; font-family: "Mulish", sans-serif; color: var(--ink); }

  .label {
    position: absolute; width: 309px; height: 371px;
    background: var(--paper); overflow: hidden;
  }
  .label.is-argan { --accent: var(--argan); --art: var(--argan-art); }
  .label.is-jojoba { --accent: var(--jojoba); --art: var(--jojoba-art); }
  .label.is-rounded { border-radius: 16px; }

  .pos-tl { left: 289px; top: 182px; }
  .pos-tr { left: 639px; top: 182px; }
  .pos-bl { left: 289px; top: 623px; }
  .pos-br { left: 639px; top: 623px; }

  .brand-mark {
    position: absolute; left: 50%; top: 13px; transform: translateX(-50%);
    width: 50px; height: 50px; border-radius: 50%;
    border: 3px solid var(--accent);
  }
  .brand-name {
    position: absolute; left: 0; right: 0; top: 69px; text-align: center;
    font-size: 33px; font-weight: 400; color: var(--accent); line-height: 1;
  }
  .purity {
    position: absolute; left: 94px; top: 108px; width: 120px; height: 25px;
    background: var(--accent); color: #fff; text-align: center;
    font-size: 19px; line-height: 25px; font-weight: 400;
  }
  .purity .script { font-family: "Great Vibes", cursive; font-size: 20px; }
  .origin {
    position: absolute; left: 0; right: 0; top: 136px; text-align: center;
    font-size: 9.5px; line-height: 11px; letter-spacing: 2px;
  }
  .product-name {
    position: absolute; left: 0; right: 0; top: 140px; text-align: center;
    font-family: "Great Vibes", cursive; font-weight: 400;
    font-size: 46px; line-height: 50px; white-space: nowrap;
  }
  .is-argan .product-name { top: 146px; }
  .uses {
    position: absolute; left: 0; right: 0; top: 199px; text-align: center;
    font-size: 10px; line-height: 12px; letter-spacing: 0.8px;
  }
  .botanical {
    position: absolute; left: 90px; top: 232px; width: 140px; height: 94px;
    background: var(--art); border-radius: 50% 40% 45% 50%;
  }
  .origin-city {
    position: absolute; left: 60px; top: 333px; font-size: 11px; line-height: 13px; font-weight: 300;
  }
  .volume {
    position: absolute; right: 28px; top: 327px; font-size: 17px; line-height: 20px; font-weight: 300;
  }
  .side-note {
    position: absolute; bottom: 26px; font-size: 10px; font-weight: 300;
    writing-mode: vertical-rl; transform: rotate(180deg); white-space: nowrap;
  }
  .side-note.is-left { left: 12px; }
  .side-note.is-right { right: 8px; }
  .web-band {
    position: absolute; left: 0; right: 0; bottom: 0; height: 20px;
    background: var(--accent); color: #fff; text-align: center;
    font-size: 11px; font-weight: 700; letter-spacing: 1.3px; line-height: 20px;
  }
</style>
</head>
<body>

<section class="label is-argan pos-tl">
  <div class="brand-mark"></div>
  <div class="brand-name">Vorisalu</div>
  <div class="purity">100% <span class="script">Pure</span></div>
  <div class="origin">MOROCCAN</div>
  <h2 class="product-name">Argan Oil</h2>
  <p class="uses">Face, Body &amp; Hair</p>
  <div class="botanical" role="img" aria-label="Ink drawing of an argan branch with green leaves and fruit"></div>
  <p class="origin-city">Larkfield IL</p>
  <p class="volume">50 mL</p>
  <p class="side-note is-left">For External Use only</p>
  <p class="side-note is-right">Ingredient: Argania Spinosa (Argan) Kernel Oil</p>
  <div class="web-band">www.vorisalu.com</div>
</section>

<section class="label is-jojoba pos-tr">
  <div class="brand-mark"></div>
  <div class="brand-name">Vorisalu</div>
  <div class="purity">100% <span class="script">Pure</span></div>
  <h2 class="product-name">Jojoba Oil</h2>
  <p class="uses">Face, Body &amp; Hair</p>
  <div class="botanical" role="img" aria-label="Ink drawing of a jojoba branch with green leaves and seed pods"></div>
  <p class="origin-city">Larkfield IL</p>
  <p class="volume">118 mL</p>
  <p class="side-note is-left">For External Use only</p>
  <p class="side-note is-right">Ingredient: Simmondsia Chinensis (Jojoba) Seed Oil</p>
  <div class="web-band">www.vorisalu.com</div>
</section>

<section class="label is-jojoba is-rounded pos-bl">
  <div class="brand-mark"></div>
  <div class="brand-name">Vorisalu</div>
  <div class="purity">100% <span class="script">Pure</span></div>
  <h2 class="product-name">Jojoba Oil</h2>
  <p class="uses">Face, Body &amp; Hair</p>
  <div class="botanical" role="img" aria-label="Ink drawing of a jojoba branch with green leaves and seed pods"></div>
  <p class="origin-city">Larkfield IL</p>
  <p class="volume">118 mL</p>
  <p class="side-note is-left">For External Use only</p>
  <p class="side-note is-right">Ingredient: Simmondsia Chinensis (Jojoba) Seed Oil</p>
  <div class="web-band">www.vorisalu.com</div>
</section>

<section class="label is-argan is-rounded pos-br">
  <div class="brand-mark"></div>
  <div class="brand-name">Vorisalu</div>
  <div class="purity">100% <span class="script">Pure</span></div>
  <div class="origin">MOROCCAN</div>
  <h2 class="product-name">Argan Oil</h2>
  <p class="uses">Face, Body &amp; Hair</p>
  <div class="botanical" role="img" aria-label="Ink drawing of an argan branch with green leaves and fruit"></div>
  <p class="origin-city">Larkfield IL</p>
  <p class="volume">50 mL</p>
  <p class="side-note is-left">For External Use only</p>
  <p class="side-note is-right">Ingredient: Argania Spinosa (Argan) Kernel Oil</p>
  <div class="web-band">www.vorisalu.com</div>
</section>

</body>
</html>
```